Design me a Business Card

We are looking for a business card design. The logo at the moment is very poor, would appreciate if you enhance that too. I have attached a cutlery image if you want to use that like sticking out from the bottom.

The content is as follows:

BV CATERING CONSULTING LIMITED
Director: MR DARIEN VELTMORE
(I will private message phone number and email once job has been awarded)

Quote at the center:

"Teamwork, leadership, respect, trust and commitment...the perfect combination for a successful catering business"
"Let us help you build the perfect catering business"

Thanks for your entries in advance

```html
<!DOCTYPE html>
<html lang="en">
<head>
<meta charset="utf-8">
<title>BV Catering Consulting Limited – Business Card</title>
<link href="https://fonts.googleapis.com/css2?family=Montserrat:wght@400;500;700&display=swap" rel="stylesheet">
<style>
  :root {
    --backdrop: #8a8787;
    --brand-red: #d72d3a;
    --card-white: #f7f7f7;
    --ink-grey: #55575a;
    --ink-dark: #3b3c3e;
    --white: #ffffff;
    --gold: #d9a23a;
    --silver: #b9bcc0;
  }
  * { box-sizing: border-box; margin: 0; padding: 0; }
  html, body {
    width: 1181px;
    height: 1200px;
    overflow: hidden;
  }
  body {
    background: var(--backdrop);
    font-family: "Montserrat", Arial, sans-serif;
    position: relative;
  }
  .card {
    position: absolute;
    width: 487px;
    height: 277px;
    border-radius: 26px;
    overflow: hidden;
  }
  .card--front {
    left: 347px;
    top: 318px;
    background: var(--brand-red);
    color: var(--white);
    text-align: center;
  }
  .card--back {
    left: 355px;
    top: 638px;
    background: var(--card-white);
  }
  .cutlery-art {
    position: absolute;
    border-radius: 4px;
  }
  .card--front .cutlery-art {
    left: 178px;
    top: 41px;
    width: 131px;
    height: 70px;
    background: linear-gradient(90deg, var(--gold), #e7c071 30%, var(--white) 55%, var(--silver) 75%, #e9e9eb);
  }
  .card--back .cutlery-art {
    left: 384px;
    top: 168px;
    width: 62px;
    height: 86px;
    background: linear-gradient(90deg, #cfd2d5, #8e9296 50%, #d6d8da);
  }
  .company-name {
    position: absolute;
    left: 0;
    right: 0;
    font-weight: 700;
    font-size: 18px;
    letter-spacing: 0.1px;
    text-align: center;
  }
  .card--front .company-name { top: 118px; color: var(--white); }
  .card--back .company-name { top: 118px; color: var(--brand-red); }
  .quote {
    position: absolute;
    left: 80px;
    right: 80px;
    top: 143px;
    font-size: 14px;
    line-height: 17px;
    font-weight: 400;
  }
  .brand-mark {
    position: absolute;
    left: 0;
    right: 0;
    top: 38px;
    display: flex;
    justify-content: center;
    align-items: center;
    gap: 12px;
  }
  .brand-dot {
    width: 30px;
    height: 30px;
    border-radius: 50%;
    background: var(--brand-red);
  }
  .brand-name {
    font-weight: 700;
    font-size: 30px;
    line-height: 36px;
    color: var(--ink-grey);
  }
  .contact-person {
    position: absolute;
    left: 31px;
    top: 164px;
  }
  .person-name {
    font-weight: 700;
    font-size: 19px;
    color: var(--ink-grey);
    line-height: 22px;
  }
  .person-role {
    font-weight: 700;
    font-size: 13px;
    color: var(--brand-red);
    line-height: 18px;
  }
  .contact-list {
    list-style: none;
    margin-top: 8px;
  }
  .contact-list li {
    display: flex;
    align-items: center;
    gap: 8px;
    font-size: 14px;
    font-weight: 500;
    color: var(--ink-dark);
    line-height: 19px;
  }
  .contact-list svg { width: 13px; height: 13px; flex: none; }
</style>
</head>
<body>
  <section class="card card--front" aria-label="Business card front">
    <div class="cutlery-art" role="img" aria-label="Row of gold and silver cutlery"></div>
    <h1 class="company-name">BV CATERING CONSULTING LIMITED</h1>
    <p class="quote">"Teamwork, leadership, respect, trust and commitment...the perfect combination for a successful catering business"<br>"Let us help you build the perfect catering business</p>
  </section>

  <section class="card card--back" aria-label="Business card back">
    <div class="brand-mark">
      <span class="brand-dot" aria-hidden="true"></span>
      <span class="brand-name">BV</span>
    </div>
    <h2 class="company-name">BV CATERING CONSULTING LIMITED</h2>
    <div class="contact-person">
      <p class="person-name">MR DARIEN VELTMORE</p>
      <p class="person-role">DIRECTOR</p>
      <ul class="contact-list">
        <li>
          <svg viewBox="0 0 24 24" aria-hidden="true"><path fill="#d72d3a" d="M6.6 10.8a15.1 15.1 0 0 0 6.6 6.6l2.2-2.2a1 1 0 0 1 1-.25 11.4 11.4 0 0 0 3.6.57 1 1 0 0 1 1 1V20a1 1 0 0 1-1 1A17 17 0 0 1 3 4a1 1 0 0 1 1-1h3.5a1 1 0 0 1 1 1c0 1.250.2 2.450.57 3.570a1 1 0 0 1-.25 1z"/></svg>
          <span>07400912384</span>
        </li>
        <li>
          <svg viewBox="0 0 24 24" aria-hidden="true"><path fill="#d72d3a" d="M2 11 22 2l-9 20-2.5-8z"/></svg>
          <span>bv.catering.consulting.ltd@example.com</span>
        </li>
      </ul>
    </div>
    <div class="cutlery-art" role="img" aria-label="Silver cutlery set standing upright"></div>
  </section>
</body>
</html>
```